Business Card, Stationary with Shark Logo for Personal Injury Lawyer

I need business cards and stationery with a shark logo for my Personal Injury Law Practice. Has to have this written on it:
Martin K. Hollis
Injury Lawyer
The Corvell Building
718 Tandy Street
Providence, Rhode Island 02908
401-627-4193
Martinhollis.com

Contact Information for Business Card

Martin K. Hollis, Injury Lawyer, address, 401-627-4193, martinhollis.com

```html
<!DOCTYPE html>
<html lang="en">
<head>
<meta charset="utf-8">
<title>Martin K. Hollis – Business Card</title>
<link rel="stylesheet" href="https://fonts.googleapis.com/css2?family=Montserrat:wght@800&family=Arimo:wght@400&display=swap">
<style>
  :root {
    --navy: #28265f;
    --grey: #9d9d9d;
    --ink: #333333;
    --paper: #ffffff;
    --backdrop: #e9e7e3;
  }
  * { margin: 0; padding: 0; box-sizing: border-box; }
  html, body { width: 1200px; height: 900px; overflow: hidden; }
  body {
    background: var(--backdrop);
    display: flex;
    flex-direction: column;
    align-items: center;
    justify-content: center;
    gap: 50px;
  }
  .card {
    position: relative;
    width: 630px;
    height: 360px;
    overflow: hidden;
    box-shadow: 0 6px 18px rgba(0,0,0,0.18);
  }
  .card-back {
    background: var(--navy);
    display: flex;
    align-items: center;
    justify-content: center;
  }
  .brand {
    display: flex;
    align-items: center;
    gap: 14px;
  }
  .brand-mark {
    flex: none;
    display: block;
  }
  .brand-name {
    font-family: "Montserrat", sans-serif;
    font-weight: 800;
    text-transform: uppercase;
    line-height: 1;
    letter-spacing: 0.01em;
  }
  .card-back .brand-mark { width: 58px; height: 58px; background: var(--paper); }
  .card-back .brand-name { color: var(--paper); font-size: 52px; }

  .card-front { background: var(--paper); }
  .card-front .wave { position: absolute; inset: 0; }
  .card-front .brand {
    position: absolute;
    right: 34px;
    top: 40px;
    gap: 10px;
  }
  .card-front .brand-mark { width: 34px; height: 34px; background: var(--navy); }
  .card-front .brand-name { color: var(--navy); font-size: 28px; }

  .holder {
    position: absolute;
    left: 44px;
    top: 44px;
  }
  .holder-name {
    font-family: "Montserrat", sans-serif;
    font-weight: 800;
    font-size: 22px;
    line-height: 1.1;
    color: var(--navy);
    text-transform: uppercase;
  }
  .holder-title {
    font-family: "Arimo", sans-serif;
    font-size: 16px;
    color: var(--ink);
    margin-top: 3px;
  }
  .contact {
    position: absolute;
    left: 44px;
    top: 128px;
    list-style: none;
    font-family: "Arimo", sans-serif;
    font-size: 15px;
    line-height: 1.3;
    color: var(--ink);
  }
  .contact li { display: flex; align-items: flex-start; gap: 8px; margin-bottom: 6px; }
  .contact .domain { color: var(--navy); }
  .contact svg { width: 20px; height: 20px; flex: none; }
</style>
</head>
<body>
  <section class="card card-back">
    <div class="brand">
      <span class="brand-mark" aria-hidden="true"></span>
      <p class="brand-name">Martin K.<br>Hollis</p>
    </div>
  </section>

  <section class="card card-front">
    <svg class="wave" viewBox="0 0 630 360" preserveAspectRatio="none" aria-hidden="true">
      <path fill="var(--grey)" d="M0,312 C200,308 340,278 460,198 C540,156 590,146 630,144 L630,360 L0,360 Z"/>
      <path fill="var(--navy)" d="M0,336 C210,328 350,296 470,211 C545,164 595,152 630,150 L630,360 L0,360 Z"/>
    </svg>

    <div class="holder">
      <h1 class="holder-name">Martin K. Hollis</h1>
      <p class="holder-title">Injury Lawyer</p>
    </div>

    <div class="brand">
      <span class="brand-mark" aria-hidden="true"></span>
      <p class="brand-name">Martin K.<br>Hollis</p>
    </div>

    <ul class="contact">
      <li>
        <svg viewBox="0 0 22 22" aria-hidden="true">
          <rect width="22" height="22" fill="var(--navy)"/>
          <path d="M7,4.5 L9.5,4.5 L10.5,8 L9,9.2 C9.8,11 11,12.2 12.8,13 L14,11.5 L17.5,12.5 L17.5,15 C17.5,16.2 16.5,17.5 15,17.5 C9.5,17 5,12.5 4.5,7 C4.5,5.5 5.8,4.5 7,4.5 Z" fill="#fff"/>
        </svg>
        <span>401-627-4193</span>
      </li>
      <li>
        <svg viewBox="0 0 22 22" aria-hidden="true">
          <rect width="22" height="22" fill="var(--navy)"/>
          <rect x="4" y="6" width="14" height="10" fill="none" stroke="#fff" stroke-width="1.4"/>
          <path d="M4,6 L11,12 L18,6" fill="none" stroke="#fff" stroke-width="1.4"/>
        </svg>
        <span>Martin@martinhollis.com</span>
      </li>
      <li>
        <svg viewBox="0 0 22 22" aria-hidden="true">
          <rect width="22" height="22" fill="var(--navy)"/>
          <circle cx="11" cy="11" r="7" fill="none" stroke="#fff" stroke-width="1.3"/>
          <ellipse cx="11" cy="11" rx="3" ry="7" fill="none" stroke="#fff" stroke-width="1.1"/>
          <path d="M4,11 H18 M5.5,7.5 H16.5 M5.5,14.5 H16.5" stroke="#fff" stroke-width="1"/>
        </svg>
        <span>www.<span class="domain">Martinhollis</span>.com</span>
      </li>
      <li>
        <svg viewBox="0 0 22 22" aria-hidden="true">
          <rect width="22" height="22" fill="var(--navy)"/>
          <path d="M11,18 C8,14 6,11.5 6,9 A5,5 0 0 1 16,9 C16,11.5 14,14 11,18 Z" fill="#fff"/>
          <circle cx="11" cy="9" r="1.8" fill="var(--navy)"/>
        </svg>
        <span>The Corvell Building, 718 Tandy Street<br>Providence, Rhode Island 02908</span>
      </li>
    </ul>
  </section>
</body>
</html>
```